- Morvandi Customer Service Signs
- 60 year old financial services firm in Boston's financial district, stock brokers are our clients, we've young/energetic employees and it's critical they provide unbeatable customer service to the brokers, family atmosphere

```html
<!DOCTYPE html>
<html lang="en">
<head>
<meta charset="UTF-8">
<title>Morvandi Customer Service Sign</title>
<link rel="stylesheet" href="https://fonts.googleapis.com/css2?family=Poppins:wght@700;800&display=swap">
<style>
  :root {
    --ink: #050505;
    --outline: #ffffff;
    --green: #6fa83a;
    --yellow: #ece21c;
    --orange: #f07a2a;
    --red-orange: #ea4f2a;
    --pink: #f59ab0;
    --cream: #fff6e6;
    --white: #ffffff;
  }
  html, body {
    margin: 0;
    padding: 0;
    overflow: hidden;
    background: var(--white);
  }
  .sign {
    position: relative;
    width: 943px;
    height: 1200px;
    overflow: hidden;
  }
  .sign__backdrop {
    position: absolute;
    inset: 0;
    background:
      radial-gradient(circle at 8% 25%, var(--yellow) 0, rgba(236,226,28,0) 22%),
      radial-gradient(circle at 5% 3%, var(--green) 0, rgba(111,168,58,0) 25%),
      radial-gradient(circle at 78% 78%, var(--white) 0, rgba(255,255,255,0.9) 22%, rgba(255,255,255,0) 55%),
      radial-gradient(circle at 5% 78%, var(--pink) 0, rgba(245,154,176,0) 30%),
      radial-gradient(circle at 90% 10%, var(--orange) 0, rgba(240,122,42,0) 35%),
      radial-gradient(circle at 20% 45%, var(--red-orange) 0, rgba(234,79,42,0) 30%),
      linear-gradient(170deg, var(--orange) 0%, #f4a860 35%, #fbd9c0 60%, var(--cream) 85%);
  }
  .sign__headline {
    position: absolute;
    left: 0;
    right: 0;
    top: 348px;
    margin: 0;
    font-family: "Poppins", sans-serif;
    font-weight: 800;
    color: var(--ink);
    -webkit-text-stroke: 9px var(--outline);
    paint-order: stroke fill;
    line-height: 1;
    letter-spacing: -1px;
  }
  .sign__line {
    display: block;
    white-space: nowrap;
  }
  .sign__line--first {
    padding-left: 52px;
    font-size: 100px;
  }
  .sign__lead {
    font-size: 66px;
    letter-spacing: 0;
  }
  .sign__line--second {
    padding-left: 58px;
    margin-top: 4px;
    font-size: 116px;
  }
</style>
</head>
<body>
  <main class="sign">
    <div class="sign__backdrop" role="img" aria-label="Soft bokeh background of glowing circles in green, yellow, orange and pink fading to white"></div>
    <h1 class="sign__headline">
      <span class="sign__line sign__line--first"><span class="sign__lead">A Rep’s </span>Perception</span>
      <span class="sign__line sign__line--second">is Your Reality</span>
    </h1>
  </main>
</body>
</html>
```